Storm Restoration Contractor needs a professional business card design

Looking for a professional business card design. Not looking for your cheapo MS Word standard ones that are readily available. Dont want it to be cookie cutter look like ones readily available online. We just recently changed our logo and want to freshen up all our documents. Our company handles restoring a property back to a pre-loss condition after a storm damages it. For example, wind, hail, flood, fire losses.

Target Market(s)

Property Owners, Homeowners, Property Owners, Commercial Property Owners, Property Management Companies, Hail and Wind Damaged Properties

Industry/Entity Type

Construction Company

Contact Information for Business Card

Halden Facades
847-519-4073
847-519-6294 fax
www.haldenfacades.example
info@haldenfacades.example

Requirements
Must have
• Clean, Professional, fresh look
• Storm Restoration, Roofing, Siding, Windows
Nice to have
• If there is a way to incorporate storms that may be cool.

```html
<!DOCTYPE html>
<html lang="en">
<head>
<meta charset="utf-8">
<title>Halden Facades — Business Card</title>
<link rel="stylesheet" href="https://fonts.googleapis.com/css2?family=Source+Sans+3:wght@400;600&display=swap">
<style>
  :root {
    --backdrop: #3a322e;
    --card: #0c0c0d;
    --blue: #1f80d1;
    --silver: #c8c8c8;
    --white: #f2f2f2;
  }
  * { margin: 0; padding: 0; box-sizing: border-box; }
  html, body { width: 1200px; height: 900px; overflow: hidden; }
  body {
    background: var(--backdrop);
    font-family: "Source Sans 3", "Myriad Pro", sans-serif;
    position: relative;
  }
  .card {
    position: absolute;
    top: 290px;
    width: 540px;
    height: 310px;
    background: var(--card);
    box-shadow: 0 10px 30px rgba(0,0,0,.45);
  }
  .card--front { left: 45px; }
  .card--back { left: 615px; display: flex; align-items: center; justify-content: center; gap: 18px; }

  .brand-dot {
    width: 96px; height: 96px; border-radius: 50%;
    border: 10px solid var(--blue);
    flex: none;
  }
  .brand-name {
    color: var(--blue);
    font-weight: 600;
    font-size: 34px;
    letter-spacing: 1px;
    text-transform: uppercase;
  }

  .front-brand {
    position: absolute; left: 36px; top: 62px;
    width: 180px;
    display: flex; flex-direction: column; align-items: center; gap: 10px;
  }
  .front-brand .brand-dot { width: 110px; height: 110px; border-width: 12px; }
  .front-brand .brand-name { font-size: 19px; letter-spacing: .5px; }

  .divider {
    position: absolute; left: 238px; top: 48px;
    width: 1px; height: 150px; background: var(--blue);
  }
  .contact { position: absolute; left: 262px; top: 44px; }
  .contact__name { color: var(--blue); font-weight: 600; font-size: 18px; line-height: 1.1; }
  .contact__role { color: var(--white); font-size: 14px; margin-bottom: 22px; }
  .contact__list { list-style: none; }
  .contact__list li {
    display: flex; align-items: center; gap: 9px;
    color: var(--silver); font-size: 14.5px; line-height: 20px;
  }
  .contact__list svg { width: 12px; height: 12px; fill: var(--blue); flex: none; }

  .services {
    position: absolute; left: 36px; right: 30px; bottom: 34px;
    color: var(--blue); font-size: 19px; letter-spacing: .2px;
  }
</style>
</head>
<body>

<section class="card card--front" aria-label="Business card front">
  <div class="front-brand">
    <div class="brand-dot"></div>
    <div class="brand-name">Halden Facades</div>
  </div>
  <div class="divider"></div>
  <div class="contact">
    <p class="contact__name">Marcus Hale</p>
    <p class="contact__role">Managing Director</p>
    <ul class="contact__list">
      <li><svg viewBox="0 0 12 12"><path d="M2.4 0.5l2 2.2-1 1.3c.7 1.6 1.9 2.8 3.5 3.6l1.3-1 2.3 2-1.2 2c-4.5-.6-8-4.1-8.6-8.6z"/></svg>847-519-4073</li>
      <li><svg viewBox="0 0 12 12"><path d="M3 0h6v3H3zM1 4h10v5H9V7H3v2H1zM3.5 8h5v4h-5z"/></svg>847-519-6294</li>
      <li><svg viewBox="0 0 12 12"><path d="M0 2h12v1.2L6 7 0 3.2zM0 4.6l6 3.8 6-3.8V10H0z"/></svg>info@haldenfacades.example</li>
      <li><svg viewBox="0 0 12 12"><circle cx="6" cy="6" r="6"/></svg>www.haldenfacades.example</li>
    </ul>
  </div>
  <p class="services">Storm Restoration | Roofing | Siding | Windows</p>
</section>

<section class="card card--back" aria-label="Business card back">
  <div class="brand-dot"></div>
  <div class="brand-name">Halden Facades</div>
</section>

</body>
</html>
```